Design Creative Banner or Gif Ads. 3 Designs To Be Selected

Come up with some creative banner ads for stonewell.co.nz

*At least 3 different winning banners will be chosen*

Please provide banner ads / gif ads in common google ads / website banner formats.

They can be gif or static but must stand out while still maintaining clear clean text and visuals, with a premium professional feel (please avoid clip art or anything that gives a cheap message).

Please keep in mind that these will likely be small ads so text needs to be large and if there's there a lot of text then use multiple frames/ pages as submit as a gif.

Style
Minimal & clean lines
Architectural or realistic images
Avoid cartoon styles, clipart, or anything that looks cheap

Font
Nexa or Montserrat or similar

Tone
Premium, serious, trustworthy — fits new builds

Colours
Option 1: Deep Navy (trust & quality) & lighter blues and warm grey
Option 2: Open to bright colours to help the ads stand out, such as (but not limited to) bright pink with black, yellow, fluorescent green, provided the messaging is still done professionally.
Our logo is attached (Stone Well Logo)

Display Sizes
Ad specs for file sizes should be file formats like JPEG, GIF, and PNG, with animations limited to a max of 30 seconds or less.
We will need several different ad sizes provided for each of the 3 selected winning designs.

• Medium Rectangle: 300 × 250 pixels
• Leaderboard: 728 × 90 pixels
• Desktop Banner ad image: (640x360 pixels)
• Desktop Banner ad image 2: (300x600 pixels)
• Possibly one or two other sizes

Flexibility to be creative
The ad text, words, upper/lower case, layout, colour, theme, and images can be adjusted to how you think it will look best. The follow example ads are just examples of what we are after but we are keen to see what you can create.

Recommendations at this point:
1. Avoid text heavy
2. Looking for more Gif ads
3. Imaging: if possible use real stock photo's rather than AI

Themes:

1
Building Soon? Start Here
Free Build Planning Pack:
✓ Build Cost Calculator
✓ Hidden Cost Checklist
✓ Builder Comparison Guide
Build With Confidence
Download Free

2
Before You Choose A Builder
Compare Price, Scope, Risk & Value
Avoid Costly Mistakes
Choose The Right Builder With Confidence
Download The Free Guide

3
Planning A New Build?
Avoid These Common Mistakes:
✗ Hidden Exclusions
✗ Missing Scope
✗ Unrealistic Allowances
✗ Budget Blowouts
Download The Free Guide

4
Before You Buy Land
Know what it could cost to build.
Avoid Costly Building Mistakes
Download Our Free Guides

5
Know Your Build Budget?
• Free Build Cost Calculator
• Hidden Cost Checklist
• Build Planning Tools
Calculate Costs (Download)

Target Market(s)

Landowners looking to build

Industry/Entity Type

Building

Font styles to use
Other font styles liked:
• Nexa or Montserrat or similar

Requirements
Should not have
• Avoid cartoon styles, clipart, or anything that looks cheap

```html
<!DOCTYPE html>
<html lang="en">
<head>
<meta charset="utf-8">
<title>Stone Well – Know Your Build Budget? Banner Set</title>
<link rel="stylesheet" href="https://fonts.googleapis.com/css2?family=Montserrat:wght@800&family=Inter:wght@400;500&display=swap">
<style>
  :root {
    --navy: #14314f;
    --navy-deep: #12304d;
    --blue-top: #2f6f98;
    --blue-mid: #3a7aa2;
    --blue-light: #c3dcf0;
    --yellow: #ffe62b;
    --white: #ffffff;
    --page: #ffffff;
  }
  * { box-sizing: border-box; margin: 0; padding: 0; }
  html, body { width: 1200px; height: 1200px; overflow: hidden; background: var(--page); }
  .canvas { position: relative; width: 1200px; height: 1200px; }

  .headline-font { font-family: "Montserrat", sans-serif; font-weight: 800; }
  .body-font { font-family: "Inter", sans-serif; }

  /* Leaderboard */
  .leaderboard {
    position: absolute; left: 142px; top: 104px; width: 917px; height: 113px;
    background: linear-gradient(100deg, var(--blue-top) 0%, var(--blue-mid) 55%, #7aa9c9 80%, var(--blue-light) 100%);
    overflow: hidden;
  }
  .leaderboard .headline {
    position: absolute; left: 23px; top: 8px;
    font-size: 36.5px; line-height: 1.15; color: var(--yellow); white-space: nowrap;
  }
  .leaderboard .cta {
    position: absolute; left: 21px; top: 66px; width: 161px; height: 30px;
    border-radius: 15px; background: var(--navy);
    color: var(--yellow); font-size: 15.5px; line-height: 30px; text-align: center;
  }
  .leaderboard .brand {
    position: absolute; left: 206px; top: 72px;
    display: flex; align-items: center; gap: 8px;
    font-size: 14px; font-weight: 500; color: #e6eef5;
  }
  .brand-square { width: 14px; height: 14px; background: #e6eef5; }
  .leaderboard .photo-inspector {
    position: absolute; left: 560px; top: 21px; width: 92px; height: 92px;
    background: linear-gradient(180deg, #d9c25a 0%, #6d88a6 40%, #243f6c 100%);
    border-radius: 40px 40px 0 0;
    opacity: 0.9;
  }
  .leaderboard .benefits {
    position: absolute; left: 655px; top: 11px; width: 262px; height: 102px;
    background: var(--yellow); border-top-left-radius: 10px;
  }
  .leaderboard .benefits-inner {
    position: absolute; left: 3px; top: 0; right: 0; bottom: 3px;
    background: var(--navy-deep); border-top-left-radius: 9px;
  }
  .leaderboard .benefit-list {
    list-style: none; position: absolute; left: 18px; top: 9px;
    font-size: 16px; line-height: 25.5px; color: var(--white);
  }

  .benefit-list li { position: relative; padding-left: 16px; white-space: nowrap; }
  .benefit-list li::before {
    content: ""; position: absolute; left: 0; top: 50%;
    width: 4px; height: 4px; margin-top: -2px; border-radius: 50%; background: var(--white);
  }

  /* Skyscraper */
  .skyscraper {
    position: absolute; left: 411px; top: 341px; width: 378px; height: 756px;
    background: linear-gradient(180deg, var(--blue-top) 0%, var(--blue-mid) 40%, #5d93b8 60%, #9dc3e0 80%, var(--blue-light) 100%);
    overflow: hidden;
  }
  .skyscraper .photo-plans {
    position: absolute; left: 133px; top: 0; width: 245px; height: 134px;
    background: linear-gradient(200deg, #e6eaee 0%, #b9c8d6 30%, #2a6fc0 60%, rgba(40,100,180,0) 100%);
    clip-path: polygon(0 0, 100% 0, 100% 100%, 85% 100%, 10% 30%);
  }
  .skyscraper .brand {
    position: absolute; left: 25px; top: 44px;
    display: flex; align-items: center; gap: 10px;
    font-size: 22px; font-weight: 500; color: var(--white);
  }
  .skyscraper .brand .brand-square { width: 18px; height: 18px; background: var(--white); }
  .skyscraper .headline {
    position: absolute; left: 26px; top: 122px;
    font-size: 53px; line-height: 69px; color: var(--yellow);
  }
  .skyscraper .benefits {
    position: absolute; left: 19px; top: 356px; width: 359px; height: 162px;
    background: var(--yellow); border-top-left-radius: 18px;
  }
  .skyscraper .benefits-inner {
    position: absolute; left: 7px; top: 0; right: 0; bottom: 5px;
    background: var(--navy-deep); border-top-left-radius: 16px;
  }
  .skyscraper .benefit-list {
    list-style: none; position: absolute; left: 18px; top: 14px;
    font-size: 23.5px; line-height: 44px; color: var(--white);
  }
  .skyscraper .benefit-list li { padding-left: 23px; }
  .skyscraper .benefit-list li::before { width: 6px; height: 6px; margin-top: -3px; }
  .skyscraper .cta {
    position: absolute; left: 25px; top: 549px; width: 327px; height: 51px;
    border-radius: 26px; background: var(--yellow);
    box-shadow: 2px 3px 0 var(--navy);
    color: var(--navy); font-size: 24px; line-height: 51px; text-align: center;
  }
  .skyscraper .photo-inspector {
    position: absolute; left: 17px; top: 612px; width: 145px; height: 144px;
    background: linear-gradient(180deg, #e6cf4e 0%, #8fa9c4 35%, #27426f 75%, #1f58b8 100%);
    border-radius: 60px 70px 0 0;
    opacity: 0.85;
  }
  .skyscraper .web-address {
    position: absolute; right: 25px; top: 710px;
    font-size: 23.5px; color: var(--navy); white-space: nowrap;
  }
</style>
</head>
<body>
<main class="canvas">

  <section class="leaderboard" aria-label="Leaderboard banner">
    <h1 class="headline headline-font">Know Your Build Budget?</h1>
    <div class="cta headline-font">Calculate costs</div>
    <div class="brand body-font"><span class="brand-square"></span>Stone Well</div>
    <div class="photo-inspector" role="img" aria-label="Photo of a building inspector in a yellow hard hat holding a clipboard and pointing up"></div>
    <div class="benefits">
      <div class="benefits-inner">
        <ul class="benefit-list body-font">
          <li>Free Build Cost Calculator</li>
          <li>Hidden Cost Checklist</li>
          <li>Build Planning Tools</li>
        </ul>
      </div>
    </div>
  </section>

  <section class="skyscraper" aria-label="Half-page banner">
    <div class="photo-plans" role="img" aria-label="Photo of blueprint plans, a rolled drawing, a hammer and a white hard hat on a desk"></div>
    <div class="brand body-font"><span class="brand-square"></span>Stone Well</div>
    <h2 class="headline headline-font">Know<br>Your Build<br>Budget?</h2>
    <div class="benefits">
      <div class="benefits-inner">
        <ul class="benefit-list body-font">
          <li>Free Build Cost Calculator</li>
          <li>Hidden Cost Checklist</li>
          <li>Build Planning Tools</li>
        </ul>
      </div>
    </div>
    <div class="cta headline-font">Calculate costs</div>
    <div class="photo-inspector" role="img" aria-label="Photo of a building inspector in a yellow hard hat holding a blue clipboard and pointing up"></div>
    <p class="web-address body-font">StoneWell.co.nz</p>
  </section>

</main>
</body>
</html>
```